Zine template for Velvet Orchard Zine

I wanted to create a zine template in inDesign or but could use some design expertise.  I have attached my draft doc.  the zine will sometimes be 32 pages, or 40 pages (8.5inches x 11, folded in 1/2). the publicaton is photocopied so placing pages in right order is important for easier assembly. I can attach sample.
I am open to masthead improvement (velvet orchard...pages you can touch).  But needs to look more like "hand made" -not too slick.  I am open to changing icon (pen dipping in water making waves...) to something that suggests a tactile, sensory impact.
I will fill in content myself for each edition.  But need page set ups that is column grid based.  So I can play with layout.  But wanted  a core based design that can make sure each edition is coherent.
Title page-same format but of course different theme, main pic, and contents
Letter from Editor/Table of Contents-again, format same, but content will change
Need 1 double page layout with double column layout option
1 double page layout with single column layout option
Maybe one with triple column layout option.
Common page number format-using shoe icon
I like idea of common theme based header or footer on each page
Add bus card info under Brindlewick press
Needs to have at least 1/2 inch margin around edges as it is copied and don't want content to bleed off page.
REmember pages stapled so need enough space between columns in middle to allow for staple and still read content
DOes this make sense?  Essentially looking for a mag layout for zine (which is just using std letter size paper, folder, and stapled to make a zine (like a pamphlet).  I uploaded a few samples of layouts and how the pages work.
Let me know if you have questions!

```html
<!DOCTYPE html>
<html lang="en">
<head>
<meta charset="utf-8">
<title>Velvet Orchard Zine – The Truth About Nails</title>
<link rel="stylesheet" href="https://fonts.googleapis.com/css2?family=Alfa+Slab+One&family=Courier+Prime:wght@400;700&display=swap">
<style>
  :root{
    --backdrop:#e9e9e7;
    --page:#e0a19b;
    --page-edge:#d8948e;
    --violet:#a45ea8;
    --plum:#5b2a4d;
    --plum-ink:#2e1a2a;
    --blush-ink:#f3d2d3;
    --paper:#ffffff;
    --ink:#2b2226;
    --marker:#f3e23a;
    --photo-fill:#8aa98a;
  }
  *{box-sizing:border-box;margin:0;padding:0}
  html,body{width:1200px;height:800px;overflow:hidden;background:var(--backdrop)}
  body{position:relative;font-family:"Courier Prime",monospace;color:var(--ink)}

  .spread{position:absolute;left:60px;top:50px;width:1080px;height:700px;display:flex;box-shadow:0 2px 10px rgba(0,0,0,.15)}
  .page{position:relative;width:540px;height:700px;background:var(--page);overflow:hidden}
  .page--left{border-right:1px solid var(--page-edge)}

  .photo{position:absolute;background:var(--photo-fill)}
  .photo--spread-left{left:390px;top:0;width:150px;height:700px}
  .photo--spread-right{left:0;top:0;width:340px;height:700px}

  .running-head{position:absolute;top:30px;font-size:10px;font-weight:700;letter-spacing:.12em;text-transform:uppercase}
  .running-head--left{left:34px}
  .running-head--right{left:365px}
  .running-head .brand{color:var(--paper);margin:0 4px}
  .running-head .section{background:var(--marker);color:var(--ink);padding:1px 4px}

  .headline{position:absolute;left:30px;top:52px;z-index:2;font-family:"Alfa Slab One",serif;font-size:48px;line-height:1.02;color:var(--paper);-webkit-text-stroke:1.5px var(--plum-ink);letter-spacing:.04em;transform:rotate(-2deg)}
  .headline span{display:inline-block;background:var(--violet);padding:2px 12px}

  .framed-photo{position:absolute;left:44px;top:200px;width:210px;height:170px;background:var(--paper);padding:9px;transform:rotate(-3deg);box-shadow:0 2px 5px rgba(0,0,0,.25)}
  .framed-photo .photo{position:static;width:100%;height:100%}

  .column{position:absolute;font-size:11px;line-height:16px}
  .column--left{left:270px;top:190px;width:118px}
  .column--right{left:365px;top:62px;width:150px}

  .subhead{display:inline-block;background:var(--plum);color:var(--paper);font-size:9.5px;font-weight:700;letter-spacing:.08em;text-transform:uppercase;padding:2px 4px;line-height:13px;margin:0 0 6px}
  .column .body{margin-bottom:16px}
  .column .body span,.pull-quote span{-webkit-box-decoration-break:clone;box-decoration-break:clone}
  .column .body span{background:var(--paper);padding:1px 3px}

  .pull-quote{position:absolute;left:36px;top:402px;width:228px;font-size:17px;line-height:21px;color:var(--blush-ink);transform:rotate(-2deg)}
  .pull-quote span{background:var(--plum);padding:1px 3px}

  .folio{position:absolute;bottom:22px;font-size:10px;font-weight:700;letter-spacing:.14em;color:var(--paper);display:flex;align-items:center;gap:5px}
  .folio--left{left:34px}
  .folio--right{right:34px}
  .folio i{width:8px;height:8px;background:var(--marker);display:block}

  .heart-badge{position:absolute;left:112px;top:470px;width:120px;height:110px}
  .heart-badge p{position:absolute;left:22px;top:22px;width:76px;font-size:9px;line-height:11px;font-weight:700;color:var(--paper);text-align:center;letter-spacing:.05em}
</style>
</head>
<body>
<main class="spread">
  <section class="page page--left">
    <div class="photo photo--spread-left" role="img" aria-label="Photograph placeholder: landscape with a lone tree on a hill (left part)"></div>

    <p class="running-head running-head--left"><span class="brand">Velvet Orchard</span><span class="section">Section Name</span></p>

    <h1 class="headline"><span>THE TRUTH</span><br><span>ABOUT NAILS</span></h1>

    <figure class="framed-photo">
      <div class="photo" role="img" aria-label="Photograph placeholder: small tree on a rolling green hill"></div>
    </figure>

    <article class="column column--left">
      <h2 class="subhead">Article subheading</h2>
      <p class="body"><span>Kept in sent gave feel will oh it we. Has pleasure procured men laughing shutters nay. Old insipidity motionless continuing law shy partiality.</span></p>
      <h2 class="subhead">Article subheading</h2>
      <p class="body"><span>As announcing it me stimulated frequently continuing. Letter fat she you now above going stand forth. He pretty future afraid should genius spirit on.</span></p>
    </article>

    <blockquote class="pull-quote"><span>Kept in sent gave feel will oh it we. Has pleasure procured men laughing shutters nay. Old insipidity motionless continuing law shy partiality. Depending acuteness dependent eat use dejection. Unpleasing astonished discovered.</span></blockquote>

    <p class="folio folio--left"><i></i>VOLUME 1</p>
  </section>

  <section class="page page--right">
    <div class="photo photo--spread-right" role="img" aria-label="Photograph placeholder: landscape with a lone tree on a hill (right part)"></div>

    <p class="running-head running-head--right"><span class="section">Section Name</span><span class="brand">Velvet Orchard</span></p>

    <div class="heart-badge">
      <svg viewBox="0 0 120 110" width="120" height="110" aria-hidden="true">
        <path d="M60 104 C20 78 4 56 4 34 C4 16 18 4 34 4 C46 4 55 11 60 20 C65 11 74 4 86 4 C102 4 116 16 116 34 C116 56 100 78 60 104 Z" fill="var(--violet)" stroke="var(--paper)" stroke-width="3"/>
      </svg>
      <p>MADE BY HAND, FELT BY HEART, MEANT TO BE HELD</p>
    </div>

    <article class="column column--right">
      <h2 class="subhead">Article subheading</h2>
      <p class="body"><span>Of country she merry engage sudden. Hearted letters her admitted contented. Joy day enjoyed regular and. Tell take it to add. Principle now indeed affection age pleasant. Directly perceived handsome met.</span></p>
      <h2 class="subhead">Article subheading could be as long as two lines if needed</h2>
      <p class="body"><span>Kept in sent gave feel will oh it we. Has pleasure procured men laughing shutters nay. Unpleasing astonished discovered not nor shy. Morning hastened and had perceived few attempt.</span></p>
    </article>

    <p class="folio folio--right">VOLUME 1<i></i></p>
  </section>
</main>
</body>
</html>
```